Modern & Fresh Sumeray Book Cover

Need a creative e-book cover for my book.

Title: Get Sumeray Sorted
Subtitle: Learn How To Easily Choose & Enroll in the Perfect Coverage at the Perfect Time.

Target Market(s)

60-70 year olds in the United States

Font styles to use
Sans Serif

Colors
9bcb3c
33a6d7

Requirements
Must have
• Must look modern and fresh.
• Use our company colors www.BrovaMint.com

```html
<!DOCTYPE html>
<html lang="en">
<head>
<meta charset="utf-8">
<title>Get Sumeray Sorted – Book Cover</title>
<link rel="stylesheet" href="https://fonts.googleapis.com/css2?family=Lilita+One&family=Yellowtail&family=Montserrat:wght@400;600&display=swap">
<style>
  :root {
    --backdrop: #14abba;
    --paper: #ffffff;
    --brand-green: #9bcb3c;
    --brand-blue: #33a6d7;
    --ink: #111111;
    --photo-top: #f3efe9;
    --photo-mid: #c9b8a4;
    --photo-low: #ffffff;
  }
  * { margin: 0; padding: 0; box-sizing: border-box; }
  html, body {
    width: 1200px;
    height: 1200px;
    overflow: hidden;
    background: var(--backdrop);
  }
  .cover {
    position: absolute;
    left: 360px;
    top: 240px;
    width: 480px;
    height: 720px;
    background: var(--paper);
    overflow: hidden;
  }
  .cover-photo {
    position: absolute;
    left: 0;
    top: 0;
    width: 480px;
    height: 275px;
    background: linear-gradient(180deg, var(--photo-low) 0%, var(--photo-top) 25%, var(--photo-mid) 60%, var(--photo-low) 100%);
  }
  .title-top {
    position: absolute;
    left: 0;
    width: 100%;
    top: 270px;
    text-align: center;
    font-family: "Lilita One", sans-serif;
    font-size: 54px;
    line-height: 1;
    color: var(--brand-green);
    text-transform: uppercase;
    letter-spacing: -0.5px;
  }
  .title-script {
    position: absolute;
    left: 0;
    width: 100%;
    top: 318px;
    text-align: center;
    font-family: "Yellowtail", cursive;
    font-size: 128px;
    line-height: 1.2;
    color: var(--brand-blue);
  }
  .subtitle {
    position: absolute;
    left: 0;
    width: 100%;
    top: 508px;
    text-align: center;
    font-family: "Montserrat", sans-serif;
    font-size: 21px;
    line-height: 26.5px;
    color: var(--ink);
  }
  .subtitle .accent-green { color: var(--brand-green); font-weight: 600; display: block; }
  .subtitle .accent-blue { color: var(--brand-blue); font-weight: 600; display: block; }
  .subtitle .plain { display: block; }
  .publisher {
    position: absolute;
    left: 0;
    width: 100%;
    top: 650px;
    display: flex;
    justify-content: center;
    align-items: center;
    gap: 8px;
  }
  .publisher-dot {
    width: 14px;
    height: 14px;
    border-radius: 50%;
    background: var(--brand-blue);
  }
  .publisher-name {
    font-family: "Montserrat", sans-serif;
    font-weight: 600;
    font-size: 28px;
    color: var(--brand-green);
  }
</style>
</head>
<body>
  <main class="cover">
    <div class="cover-photo" role="img" aria-label="Four smiling seniors sitting on rope swings against a white background"></div>
    <h1>
      <span class="title-top">Get Sumeray</span>
      <span class="title-script">Sorted</span>
    </h1>
    <p class="subtitle">
      <span class="plain">Learn How To</span>
      <span class="accent-green">Easily Choose &amp; Enroll</span>
      <span class="accent-blue">in the Perfect Coverage</span>
      <span class="plain">at the Perfect Time</span>
    </p>
    <div class="publisher">
      <span class="publisher-dot"></span>
      <span class="publisher-name">BrovaMint</span>
    </div>
  </main>
</body>
</html>
```